Technology Company Web Design Project

We are working with BrimCore. They are a technology company and in need of a new website design.
BrimCore helps companies control who (or what) can access which information inside their systems — and under what conditions. Think of them as the traffic controller for digital access and data permissions.
Instead of letting every app, employee, or AI bot freely connect to everything, GatewardIQ makes sure:
• Each one only gets access to what it actually needs.
• That access follows company rules automatically.
• Those rules are enforced the same way everywhere — across apps, servers, and even AI tools.
Some competitor sites to use for inspiration:
https://www.trovanexus.example/en/lp/ac/trovaspire.html
https://www.clearrulekeeper.example
https://www.vondix.example
Thank you for taking the time to consider designing a website for us. We are web developers based in Stockton and Los Angeles, CA, USA. Most of our projects go through the same process. Understanding this process may help you win a project with us. We custom-code all of our websites in-house. We don’t have any requirements as to what tools you use for your design, but we prefer Drafton files. For any design that we label as four-stars, we send it to the client for review. The client picks the final design they want us to use. Once we complete this process, we will continue to show additional clients all the four-star sites and purchase them later. Your designs will have multiple chances to sell. For better chances of success, we ask that you follow these guidelines.
IMAGES:
If you use any images or icons in the design, we ask that you have a link to the asset so we can purchase the image/icon. Most of the designs we submit do not have the customer’s images on them unless they have some great images. Be creative; show us the feeling you are trying to portray with your image choices. Use any royalty-free site you choose. We subscribe to Kelvaro and mainly use their images, but we can purchase images outside of Kelvaro.
PLEASE NOTE: we will not submit designs to clients with watermarks on the images.
FONTS:
We ask that you identify the fonts used in the design. This can be done in a message if you want. We typically use Quillny Fonts and Kelvaro Fonts.
CONTENT:
We're always open to different content and ideas. We often submit designs with stock images so the client can see our vision. We typically take pictures after the website launch to use their images with our vision. Lorem Ipsum is fine for paragraphs, but we ask that you write the headers in correct English. We want to be able to show the vision and identify the sections of the website.
INSPIRATION:
We typically add a couple of links in the brief of websites we like to help you get started in your design.
REVISIONS:
We do not often ask for revisions of the designs unless we see something in the design that may not appeal to the client. If there are slight changes that we want to make, we do that in the development process.
FEEDBACK:
We rarely give feedback on designs during the design process. We are working on many website projects and do not have the time to provide feedback. We usually respond if your request is well thought out and asks specific questions, but a note asking “feedback, please” usually goes unanswered.

```html
<!DOCTYPE html>
<html lang="en">
<head>
<meta charset="utf-8">
<title>BrimCore — GatewardIQ</title>
<link rel="stylesheet" href="https://fonts.googleapis.com/css2?family=Plus+Jakarta+Sans:wght@400;500;600;700;800&display=swap">
<style>
:root{
  --navy:#1f3a5f;
  --navy-deep:#1c365a;
  --orange:#e8802f;
  --orange-soft:#fbeadb;
  --peach:#fdf3ea;
  --grey-card:#e9edf1;
  --band:#e8edf2;
  --text:#1f2a3a;
  --muted:#5a6473;
  --white:#ffffff;
  --yellow:#fdf3a6;
}
*{box-sizing:border-box;margin:0;padding:0}
html,body{width:1200px;height:3856px;overflow:hidden}
body{position:relative;font-family:"Plus Jakarta Sans",Arial,sans-serif;color:var(--text);background:var(--white)}
.abs{position:absolute}
a{color:inherit}

/* hero */
.hero{position:absolute;left:0;top:0;width:1200px;height:751px;
  background:linear-gradient(180deg,#fff 0%,#fff8f2 55%,#fdf0e4 100%)}
.hero-grid{position:absolute;left:560px;top:0;width:640px;height:560px;
  background-image:repeating-linear-gradient(0deg,rgba(232,128,47,.08) 0 1px,transparent 1px 28px),
  repeating-linear-gradient(90deg,rgba(232,128,47,.08) 0 1px,transparent 1px 28px);
  -webkit-mask-image:radial-gradient(ellipse at 60% 40%,#000 30%,transparent 75%);
  mask-image:radial-gradient(ellipse at 60% 40%,#000 30%,transparent 75%)}
.brand{left:92px;top:44px;display:flex;align-items:center;gap:10px}
.brand-dot{width:18px;height:18px;border-radius:50%;background:var(--orange)}
.brand-name{font-weight:800;font-size:24px;color:var(--navy);letter-spacing:.5px}
.nav{left:352px;top:42px;display:flex;gap:21px;font-size:11px;font-weight:500;color:var(--navy);align-items:center}
.nav .home{width:14px;height:14px}
.btn{display:inline-flex;align-items:center;justify-content:space-between;border-radius:22px;
  font-size:10.5px;font-weight:700;letter-spacing:.3px;color:#fff;text-transform:uppercase}
.btn .arr{width:28px;height:28px;border-radius:50%;display:flex;align-items:center;justify-content:center}
.btn-orange{background:var(--orange)}
.btn-orange .arr{background:var(--navy)}
.btn-navy{background:var(--navy)}
.btn-navy .arr{background:var(--orange)}
.nav-cta{left:940px;top:30px;width:170px;height:40px;padding:0 6px 0 24px}
.hero-title{left:90px;top:252px;font-size:46px;line-height:50px;font-weight:700;color:var(--navy);letter-spacing:-.5px}
.hero-title .o{color:var(--orange)}
.hero-text{left:90px;top:418px;width:420px;font-size:11px;line-height:17px;color:var(--muted)}
.hero-btn1{left:90px;top:480px;width:146px;height:40px;padding:0 6px 0 24px}
.hero-btn2{left:245px;top:480px;width:170px;height:40px;padding:0 6px 0 24px}

.customers{left:600px;top:218px;width:506px;height:364px;background:#fff;border:1.5px solid #b9c3cf;border-radius:18px;box-shadow:0 10px 30px rgba(31,58,95,.08)}
.customers h3{position:absolute;left:25px;top:26px;font-size:18px;font-weight:600;color:var(--navy)}
.sort{position:absolute;right:26px;top:30px;font-size:13px;color:var(--navy)}
.row{position:absolute;left:8px;width:490px;height:72px;display:flex;align-items:center;padding-left:20px;border-radius:12px}
.row.active{background:var(--yellow)}
.avatar{width:36px;height:36px;border-radius:50%;margin-right:14px}
.row .nm{font-size:14px;font-weight:500;color:var(--navy)}
.row .co{font-size:11.5px;color:var(--muted);margin-top:2px}
.row-tools{position:absolute;right:30px;top:26px;display:flex;gap:28px}
.all{position:absolute;left:25px;top:322px;font-size:13.5px;color:var(--navy);display:flex;align-items:center;gap:8px}

.chart{left:920px;top:448px;width:240px;height:186px;background:#fff;border:1.5px solid #b9c3cf;border-radius:14px;transform:rotate(-5deg);box-shadow:0 10px 24px rgba(31,58,95,.08)}
.chart .lbl{position:absolute;left:24px;top:22px;font-size:8px;color:var(--muted)}
.chart .val{position:absolute;left:24px;top:36px;font-size:19px;font-weight:600;color:var(--navy)}
.chart .wk{position:absolute;right:22px;top:22px;font-size:8px;color:var(--muted)}
.chart .wk b{color:#e65a5a;font-weight:500}
.bars{position:absolute;left:28px;bottom:36px;display:flex;gap:14px;align-items:flex-end}
.bar{width:12px;display:flex;flex-direction:column;border-radius:2px;overflow:hidden}
.bar i{display:block}
.c1{background:#7fd8e8}.c2{background:#f5a3a3}.c3{background:#f7c948}
.days{position:absolute;left:30px;bottom:14px;display:flex;gap:19px;font-size:8px;color:var(--muted)}

/* band */
.band{left:0;top:751px;width:1200px;height:126px;background:var(--band);border-top:1px solid #d5dce4;border-bottom:1px solid #d5dce4}
.band p{position:absolute;left:180px;top:42px;width:840px;text-align:center;font-size:13.5px;line-height:20px;color:var(--navy)}

.section-title{position:absolute;left:0;width:1200px;text-align:center;font-size:32px;font-weight:700;color:var(--navy);letter-spacing:-.3px}
.section-title .o{color:var(--orange)}

.glow{position:absolute;border-radius:50%;filter:blur(60px);background:#fce2cb;opacity:.7}

.feature{position:absolute;top:1022px;width:235px;height:250px;border-radius:18px;padding:34px 38px}
.feature.grey{background:var(--grey-card)}
.feature.peach{background:var(--orange-soft)}
.ficon{width:58px;height:58px;border-radius:10px;display:flex;align-items:center;justify-content:center;margin-bottom:26px}
.ficon.navy{background:var(--navy)}
.ficon.orange{background:var(--orange)}
.feature h4{font-size:14px;line-height:20px;font-weight:700;color:var(--navy);margin-bottom:14px}
.feature p{font-size:10.5px;line-height:17px;color:var(--muted)}

/* how */
.how-item{position:absolute;width:240px}
.how-item h5{font-size:13px;font-weight:700;color:var(--navy);margin-bottom:8px}
.how-item p{font-size:10.5px;line-height:17px;color:var(--muted)}
.how-item.right{text-align:right}
.how-line{position:absolute;height:1.5px;background:var(--orange)}
.how-dot{position:absolute;width:7px;height:7px;border-radius:50%;background:var(--orange)}

/* use cases */
.cases{left:91px;top:1740px;width:1018px;height:485px;background:var(--band);border:1.5px solid #94a3b6;border-radius:44px}
.cases h2{position:absolute;left:94px;top:58px;font-size:52px;font-weight:700;color:var(--navy);letter-spacing:-.5px}
.cases h2 span{color:var(--orange)}
.circ{position:absolute;top:66px;width:40px;height:40px;border-radius:50%;display:flex;align-items:center;justify-content:center}
.case{position:absolute;top:149px;width:261px;height:270px;border-radius:16px;overflow:hidden}
.case .num{position:absolute;left:40px;top:140px;font-size:26px;font-weight:700;color:var(--orange)}
.case .tt{position:absolute;left:40px;top:188px;font-size:16px;line-height:22px;font-weight:600;color:#fff}

/* testimonial */
.quote-mark{left:296px;top:2356px;font-size:200px;line-height:200px;font-weight:800;color:var(--orange);font-family:Georgia,serif}
.testi-title{left:437px;top:2306px;font-size:32px;font-weight:700;color:var(--navy)}
.testi-title span{color:var(--orange)}
.testi-text{left:437px;top:2376px;width:480px;font-size:14px;line-height:21px;color:var(--navy)}
.testi-by{left:437px;top:2433px;font-size:13px;font-weight:600;color:var(--orange)}

.divider{position:absolute;left:0;top:2534px;width:1200px;height:1px;background:#dde3ea}

/* blogs */
.blogs-title{left:126px;top:2606px;font-size:32px;font-weight:700;color:var(--navy)}
.blogs-title span{color:var(--orange)}
.blog-btn{left:913px;top:2609px;width:161px;height:40px;padding:0 6px 0 26px}
.blog{position:absolute;top:2678px;width:302px}
.blog .img{width:302px;height:241px;border-radius:18px}
.blog h6{margin:32px 0 0 28px;font-size:16.5px;line-height:24px;font-weight:600;color:var(--navy)}
.blog .more{display:inline-block;margin:16px 0 0 28px;font-size:10px;font-weight:600;color:var(--orange);text-decoration:underline}

/* footer */
.footer{left:0;top:3136px;width:1200px;height:720px;background:var(--navy-deep);color:#fff}
.f-kicker{position:absolute;left:97px;top:120px;font-size:17px;font-weight:600}
.f-big{position:absolute;left:90px;top:148px;font-size:88px;font-weight:700;letter-spacing:-1px}
.f-news{position:absolute;left:546px;top:137px;font-size:17px;font-weight:600}
.f-input{position:absolute;left:548px;top:179px;width:388px;height:43px;background:#fff;border-radius:22px;font-size:11px;color:var(--navy);padding:15px 20px}
.f-input .go{position:absolute;right:8px;top:7px;width:30px;height:30px;border-radius:50%;background:var(--orange);display:flex;align-items:center;justify-content:center}
.f-rule{position:absolute;left:546px;top:282px;width:558px;height:1px;background:rgba(255,255,255,.25)}
.f-links{position:absolute;top:345px;list-style:none;font-size:12.5px}
.f-links li{height:30px;text-decoration:underline}
.f-info{position:absolute;left:915px;top:345px;font-size:10.5px;line-height:15px}
.f-info h6{font-size:14px;font-weight:700;margin-bottom:14px}
.f-info p{margin-bottom:8px}
.f-bottom{position:absolute;left:90px;top:629px;width:1020px;height:1px;background:rgba(255,255,255,.25)}
.f-copy{position:absolute;left:90px;top:664px;font-size:12px}
.f-copy span{color:var(--orange);font-weight:600}
.social{position:absolute;top:655px;display:flex;align-items:center;gap:12px;font-size:11px;color:#c8d2de}
.social i{width:36px;height:36px;border-radius:50%;background:#2f4b72;display:block}
.to-top{position:absolute;left:1138px;top:610px;width:40px;height:40px;border-radius:50%;background:var(--orange);display:flex;align-items:center;justify-content:center}
</style>
</head>
<body>

<header class="hero">
  <div class="hero-grid"></div>
  <div class="abs brand"><span class="brand-dot"></span><span class="brand-name">BrimCore</span></div>
  <nav class="abs nav">
    <svg class="home" viewBox="0 0 16 16"><path d="M2 8 8 2l6 6v6h-4v-4H6v4H2z" fill="#e8802f"/></svg>
    <span>Features</span><span>How It Works</span><span>Use Cases</span><span>Security &amp; Compliance</span><span>Resources</span><span>Pricing</span><span>About</span>
  </nav>
  <a class="abs btn btn-orange nav-cta">Request a demo <span class="arr"><svg width="11" height="11" viewBox="0 0 12 12"><path d="M3 9 9 3M4 3h5v5" stroke="#fff" stroke-width="1.4" fill="none"/></svg></span></a>

  <h1 class="abs hero-title">Control Access.<br><span class="o">Enforce Trust.</span><br>Wherever You Work.</h1>
  <p class="abs hero-text">GatewardIQ ensures every app, AI agent, and user gets only the access they need — automatically, securely, everywhere.</p>
  <a class="abs btn btn-orange hero-btn1">Get started <span class="arr"><svg width="11" height="11" viewBox="0 0 12 12"><path d="M3 9 9 3M4 3h5v5" stroke="#fff" stroke-width="1.4" fill="none"/></svg></span></a>
  <a class="abs btn btn-navy hero-btn2">Request a demo <span class="arr"><svg width="11" height="11" viewBox="0 0 12 12"><path d="M3 9 9 3M4 3h5v5" stroke="#fff" stroke-width="1.4" fill="none"/></svg></span></a>

  <div class="abs customers">
    <h3>Customers</h3>
    <div class="sort">Sort by Newest ▾</div>
    <div class="row active" style="top:76px">
      <div class="avatar" role="img" aria-label="Customer avatar" style="background:linear-gradient(135deg,#f08a5d,#c0392b)"></div>
      <div><div class="nm">Mira Halvorsen</div><div class="co">Dunmere Organic Co.</div></div>
      <div class="row-tools">
        <svg width="14" height="14" viewBox="0 0 16 16"><path d="M3 13l1-4 7-7 3 3-7 7z" stroke="#1f3a5f" stroke-width="1.3" fill="none"/></svg>
        <svg width="14" height="14" viewBox="0 0 16 16"><path d="M8 1.5l2 4.2 4.6.6-3.4 3.2.9 4.6L8 11.8 3.9 14l.9-4.6L1.4 6.3 6 5.7z" stroke="#1f3a5f" stroke-width="1.3" fill="none"/></svg>
        <svg width="14" height="14" viewBox="0 0 16 16"><circle cx="8" cy="8" r="6" stroke="#1f3a5f" stroke-width="1.3" fill="none"/><path d="M5 8h6" stroke="#1f3a5f" stroke-width="1.3"/></svg>
        <svg width="14" height="14" viewBox="0 0 16 16"><circle cx="8" cy="3" r="1.2" fill="#1f3a5f"/><circle cx="8" cy="8" r="1.2" fill="#1f3a5f"/><circle cx="8" cy="13" r="1.2" fill="#1f3a5f"/></svg>
      </div>
    </div>
    <div class="row" style="top:150px">
      <div class="avatar" role="img" aria-label="Customer avatar" style="background:linear-gradient(135deg,#7fcfc2,#e8a27c)"></div>
      <div><div class="nm">Colin Ashworth</div><div class="co">Marketplace Orvella</div></div>
    </div>
    <div class="row" style="top:222px">
      <div class="avatar" role="img" aria-label="Customer avatar" style="background:linear-gradient(135deg,#f7c948,#d9534f)"></div>
      <div><div class="nm">Gideon Hale</div><div class="co">Harbor Finest Produce</div></div>
    </div>
    <div class="all">All customers <svg width="14" height="14" viewBox="0 0 16 16"><circle cx="8" cy="8" r="6.5" stroke="#1f3a5f" stroke-width="1.3" fill="none"/><path d="M5.5 8h5M8.5 6l2 2-2 2" stroke="#1f3a5f" stroke-width="1.3" fill="none"/></svg></div>
  </div>

  <div class="abs chart">
    <div class="lbl">Daily Average</div>
    <div class="val">2h 20m</div>
    <div class="wk"><b>+30m</b> this week</div>
    <div class="bars">
      <div class="bar"><i class="c1" style="height:10px"></i><i class="c2" style="height:14px"></i><i class="c3" style="height:16px"></i></div>
      <div class="bar"><i class="c1" style="height:14px"></i><i class="c2" style="height:18px"></i><i class="c3" style="height:22px"></i></div>
      <div class="bar"><i class="c1" style="height:12px"></i><i class="c2" style="height:16px"></i><i class="c3" style="height:18px"></i></div>
      <div class="bar"><i class="c1" style="height:18px"></i><i class="c2" style="height:22px"></i><i class="c3" style="height:22px"></i></div>
      <div class="bar"><i class="c1" style="height:12px"></i><i class="c2" style="height:12px"></i><i class="c3" style="height:18px"></i></div>
      <div class="bar"><i class="c1" style="height:8px"></i><i class="c2" style="height:10px"></i><i class="c3" style="height:14px"></i></div>
      <div class="bar"><i class="c1" style="height:8px"></i><i class="c2" style="height:8px"></i><i class="c3" style="height:12px"></i></div>
    </div>
    <div class="days"><span>M</span><span>T</span><span>W</span><span>T</span><span>F</span><span>S</span><span>S</span></div>
  </div>
</header>

<section class="abs band">
  <p>In today’s complex systems, letting every component freely connect is risky. GatewardIQ ensures each identity gets exactly the permissions it needs, automatically enforcing your policies across apps, servers, and AI tools.</p>
</section>

<div class="glow" style="left:900px;top:1100px;width:420px;height:420px"></div>
<div class="glow" style="left:-100px;top:1500px;width:500px;height:300px;opacity:.5"></div>

<h2 class="section-title" style="top:946px">Why <span class="o">GatewardIQ</span> is different</h2>

<article class="feature grey" style="left:109px">
  <div class="ficon navy"><svg width="28" height="28" viewBox="0 0 28 28" fill="none" stroke="#fff" stroke-width="1.5"><circle cx="14" cy="10" r="5"/><path d="M4 22c3-3 6-4 10-4s7 1 10 4"/></svg></div>
  <h4>Least Privilege<br>by Default</h4>
  <p>Grant minimal access needed. Reduce attack surface, limit scope.</p>
</article>
<article class="feature peach" style="left:359px">
  <div class="ficon orange"><svg width="28" height="28" viewBox="0 0 28 28" fill="none" stroke="#fff" stroke-width="1.5"><circle cx="14" cy="14" r="4"/><circle cx="14" cy="4" r="2"/><circle cx="14" cy="24" r="2"/><circle cx="4" cy="14" r="2"/><circle cx="24" cy="14" r="2"/><path d="M14 6v4M14 18v4M6 14h4M18 14h4"/></svg></div>
  <h4>Policy-Driven Access<br>Across Platforms</h4>
  <p>Define rules once and enforce them everywhere — apps, AI, servers.</p>
</article>
<article class="feature grey" style="left:607px">
  <div class="ficon navy"><svg width="28" height="28" viewBox="0 0 28 28" fill="none" stroke="#fff" stroke-width="1.5"><circle cx="14" cy="14" r="10"/><circle cx="14" cy="14" r="5"/><circle cx="14" cy="14" r="1.5" fill="#fff"/></svg></div>
  <h4>Consistent<br>Enforcement</h4>
  <p>No gaps. Every access request is checked against your policies.</p>
</article>
<article class="feature peach" style="left:856px">
  <div class="ficon orange"><svg width="28" height="28" viewBox="0 0 28 28" fill="none" stroke="#fff" stroke-width="1.5"><path d="M7 3h10l5 5v17H7z"/><path d="M11 12h7M11 16h7M11 20h4"/></svg></div>
  <h4>Audit<br>&amp; Visibility</h4>
  <p>Full logs. Full visibility into who accessed what, when, and why.</p>
</article>

<h2 class="section-title" style="top:1372px">How it <span class="o">works</span></h2>

<svg class="abs" style="left:404px;top:1440px" width="392" height="160" viewBox="0 0 392 160" aria-hidden="true">
  <circle cx="196" cy="80" r="48" fill="none" stroke="#1f3a5f" stroke-width="2"/>
  <circle cx="196" cy="80" r="10" fill="#e8802f"/>
</svg>

<div class="how-item right" style="left:119px;top:1448px">
  <h5>Enforce Everywhere</h5>
  <p>Access decisions are evaluated in real-time, no matter where the request originates.</p>
</div>
<div class="how-dot" style="left:375px;top:1454px"></div><div class="how-line" style="left:382px;top:1457px;width:22px"></div>

<div class="how-item" style="left:838px;top:1450px">
  <h5>Define Policies</h5>
  <p>Write rules for what can access what, under which conditions (who, what, where, when).</p>
</div>
<div class="how-line" style="left:796px;top:1459px;width:30px"></div><div class="how-dot" style="left:822px;top:1456px"></div>

<div class="how-item right" style="left:242px;top:1584px">
  <h5>Monitor &amp; Audit</h5>
  <p>Track access activity, generate reports, see policy violations or anomalies.</p>
</div>
<div class="how-dot" style="left:494px;top:1590px"></div><div class="how-line" style="left:501px;top:1593px;width:100px"></div>

<div class="how-item" style="left:718px;top:1584px">
  <h5>Connect All Systems</h5>
  <p>Integrate apps, servers, APIs, AI tools, identity providers.</p>
</div>
<div class="how-line" style="left:600px;top:1593px;width:100px"></div><div class="how-dot" style="left:700px;top:1590px"></div>

<section class="abs cases">
  <h2>Use <span>Cases</span></h2>
  <div class="circ" style="left:830px;background:var(--navy)"><svg width="14" height="14" viewBox="0 0 14 14"><path d="M12 7H2M6 3 2 7l4 4" stroke="#fff" stroke-width="1.5" fill="none"/></svg></div>
  <div class="circ" style="left:879px;background:var(--orange)"><svg width="14" height="14" viewBox="0 0 14 14"><path d="M2 7h10M8 3l4 4-4 4" stroke="#fff" stroke-width="1.5" fill="none"/></svg></div>
  <div class="case" style="left:96px" role="img" aria-label="Photo of a hand holding a tablet showing a dashboard">
    <div style="position:absolute;inset:0;background:linear-gradient(180deg,#5f7f99 0%,#24466f 45%,#0f2a55 100%)"></div>
    <div class="num">01</div><div class="tt">Enterprise Apps<br>and Microservices</div>
  </div>
  <div class="case" style="left:378px" role="img" aria-label="Illustration of a glowing network cloud">
    <div style="position:absolute;inset:0;background:linear-gradient(180deg,#3a2a20 0%,#1d4660 45%,#0e2442 100%)"></div>
    <div class="num">02</div><div class="tt">Cloud / Multi-Cloud<br>Infrastructure</div>
  </div>
  <div class="case" style="left:659px" role="img" aria-label="Photo of a partner handshake in violet light">
    <div style="position:absolute;inset:0;background:linear-gradient(180deg,#7a3fd1 0%,#4c1f9e 55%,#2c0f6e 100%)"></div>
    <div class="num">03</div><div class="tt">Third-Party /<br>Partner Access</div>
  </div>
</section>

<h2 class="abs testi-title">What <span>Customers</span> Say</h2>
<div class="abs quote-mark">“</div>
<p class="abs testi-text">Since adopting GatewardIQ, unauthorized access events dropped by 85%, and our audit readiness improved dramatically.</p>
<div class="abs testi-by">Security Lead, Norvane Corp</div>

<div class="divider"></div>

<h2 class="abs blogs-title">Our Latest <span>Blogs</span></h2>
<a class="abs btn btn-orange blog-btn">View all blog <span class="arr"><svg width="11" height="11" viewBox="0 0 12 12"><path d="M3 9 9 3M4 3h5v5" stroke="#fff" stroke-width="1.4" fill="none"/></svg></span></a>

<article class="blog" style="left:126px">
  <div class="img" role="img" aria-label="Photo of a professional beside a glowing security shield interface" style="background:linear-gradient(135deg,#2c5d8f 0%,#1a3352 55%,#c8683a 100%)"></div>
  <h6>Policy-Driven Access: The Future of Security</h6>
  <a class="more">LEARN MORE</a>
</article>
<article class="blog" style="left:450px">
  <div class="img" role="img" aria-label="Photo of a finger pressing a protected scanner button" style="background:linear-gradient(135deg,#3d7a84 0%,#143a4a 50%,#0b1e2c 100%)"></div>
  <h6>Common Access Control Mistakes (and How to Avoid Them)</h6>
  <a class="more">LEARN MORE</a>
</article>
<article class="blog" style="left:772px">
  <div class="img" role="img" aria-label="Photo of an analyst working at monitors in a data center" style="background:linear-gradient(135deg,#4d6a86 0%,#223447 50%,#151d27 100%)"></div>
  <h6>How Quantrel Reduced Unauthorized Access by 80%</h6>
  <a class="more">LEARN MORE</a>
</article>

<footer class="abs footer">
  <div class="f-kicker">Tell us about your project</div>
  <div class="f-big">Let’s talk</div>
  <div class="f-news">Get the latest inspiration &amp; insights</div>
  <div class="f-input">Your Email...
    <span class="go"><svg width="12" height="12" viewBox="0 0 12 12"><path d="M1 6 11 1 7 11 6 7z" fill="#fff"/></svg></span>
  </div>
  <div class="f-rule"></div>
  <ul class="f-links" style="left:546px">
    <li>Home</li><li>Features</li><li>How It Works</li><li>Use Cases</li><li>Pricing</li><li>Resources</li><li>About Us</li><li>Contact</li>
  </ul>
  <ul class="f-links" style="left:714px">
    <li>Blog</li><li>Documentation</li><li>Tutorials</li><li>Whitepapers</li><li>Support</li>
  </ul>
  <div class="f-info">
    <h6>BRIMCORE INFO</h6>
    <p>BrimCore Headquarters<br>48 Meridian Way, Suite 210<br>Stockton, CA 95202, USA</p>
    <p>Mobile: +1 (209) 555-0147</p>
    <p>Email: hello@brimcore.example</p>
  </div>
  <div class="to-top"><svg width="14" height="14" viewBox="0 0 14 14"><path d="M7 12V2M3 6l4-4 4 4" stroke="#fff" stroke-width="1.5" fill="none"/></svg></div>
  <div class="f-bottom"></div>
  <div class="f-copy">© 2025 <span>brimcore</span> - All rights reserved</div>
  <div class="social" style="left:770px"><i></i>Friendloop</div>
  <div class="social" style="left:912px"><i></i>Chirpline</div>
  <div class="social" style="left:1031px"><i></i>Workwove</div>
</footer>

</body>
</html>
```